MEDICAL GRANT GRAPHIC FOR SCIENTIFIC STUDY

FOR A GRANT, WE NEED A GRAPHIC THAT REFLECTS THE ISSUES IN OUR GRANT.
COLORS: BLUE/GREEENS
I AM UPLOADING TWO GRAPHICS.
THE SECOND ONE IS A BALANCE WHICH NEEDS TO BE INCLUDED IN THE FIRST GRAPHIC. THE BALANCE IS EQUAL IN THE GRAPHIC I HAVE DONE. HOWEVER, FOR THE FINAL PRODUCT, THE BALANCE NEEDS TO BE LOWER ON THE END WITH 'PATIENT WORKLOAD'

Target Market(s)

GRANT FUNDERS

Font styles to use
Sans Serif

Colors
0094D4
00A9DD
6FCCEA
C7EBF8
E9F6FB

```html
<!DOCTYPE html>
<html lang="en">
<head>
<meta charset="utf-8">
<title>Medical Grant Issues</title>
<link rel="stylesheet" href="https://fonts.googleapis.com/css2?family=Barlow+Condensed:wght@700&family=Barlow+Semi+Condensed:wght@600;700&display=swap">
<style>
  :root {
    --backdrop: #303030;
    --card: #ffffff;
    --header: #00a9dd;
    --navy: #1b3a5c;
    --sky: #0aa6d6;
    --slate: #4f7a9e;
    --mint: #8fe3dd;
    --teal: #18a9b8;
    --halo: #dcdcdc;
    --arrow: #1fa3d8;
    --panel: #e9ecee;
    --panel-line: #3cb0d6;
    --white: #ffffff;
  }
  html, body {
    margin: 0;
    padding: 0;
    width: 1200px;
    height: 1177px;
    overflow: hidden;
    background: var(--backdrop);
  }
  .graphic { display: block; width: 1200px; height: 1177px; }
  .title {
    font-family: "Barlow Condensed", sans-serif;
    font-weight: 700;
    font-size: 62px;
    fill: var(--white);
    letter-spacing: 0.5px;
  }
  .label {
    font-family: "Barlow Semi Condensed", sans-serif;
    font-weight: 700;
    font-size: 11.5px;
    fill: var(--white);
  }
  .label--dark { fill: var(--navy); }
  .label--banner { font-size: 19px; font-family: "Barlow Condensed", sans-serif; }
  .flow-line { fill: none; stroke: var(--navy); stroke-width: 2.4; }
  .flow-arrow { fill: none; stroke: var(--arrow); stroke-width: 4; }
  .icon-stroke { fill: none; stroke-width: 3; stroke-linecap: round; stroke-linejoin: round; }
</style>
</head>
<body>
<svg class="graphic" viewBox="0 0 1000 981" xmlns="http://www.w3.org/2000/svg">
  <defs>
    <marker id="head-navy" viewBox="0 0 10 10" refX="8" refY="5" markerWidth="5" markerHeight="5" orient="auto">
      <path d="M0,0 L10,5 L0,10 L3,5 Z" fill="#1b3a5c"/>
    </marker>
    <marker id="head-sky" viewBox="0 0 10 10" refX="6" refY="5" markerWidth="4" markerHeight="4" orient="auto-start-reverse">
      <path d="M0,0 L10,5 L0,10 Z" fill="#1fa3d8"/>
    </marker>
  </defs>

  <!-- card -->
  <rect class="card" x="73" y="163" width="852" height="659" fill="var(--card)"/>
  <rect class="header-band" x="73" y="163" width="852" height="105" fill="var(--header)"/>
  <text class="title" x="499" y="238" text-anchor="middle">MEDICAL GRANT ISSUES</text>

  <!-- connector lines -->
  <path class="flow-line" d="M273,327 H120 V562"/>
  <path class="flow-line" d="M215,327 H186" marker-end="url(#head-navy)"/>
  <path class="flow-line" d="M120,423 H152" marker-end="url(#head-navy)"/>
  <path class="flow-line" d="M120,562 H152" marker-end="url(#head-navy)"/>
  <path class="flow-line" d="M512,349 V410" marker-end="url(#head-navy)"/>
  <path class="flow-line" d="M728,327 H773 V405" marker-end="url(#head-navy)"/>

  <!-- banner -->
  <rect class="banner" x="273" y="305" width="455" height="44" rx="22" fill="var(--navy)"/>
  <text class="label label--banner" x="500" y="334" text-anchor="middle">CONSUMER ADVISORY GROUP ENGAGEMENT</text>

  <!-- step: identifying -->
  <g class="step step--identify">
    <circle cx="198" cy="425" r="46" fill="var(--halo)"/>
    <rect x="165" y="388" width="200" height="75" rx="37.5" fill="var(--sky)"/>
    <circle cx="210" cy="425" r="30" fill="var(--white)"/>
    <circle cx="206" cy="420" r="10" class="icon-stroke" stroke="var(--sky)"/>
    <path d="M213,428 L222,438" class="icon-stroke" stroke="var(--sky)" stroke-width="5"/>
    <text class="label" text-anchor="middle"><tspan x="303" y="411">IDENTIFYING</tspan><tspan x="303" y="424">COMPLEX PATIENTS</tspan><tspan x="303" y="437">WITH RHEUMATIC</tspan><tspan x="303" y="450">DISEASES</tspan></text>
  </g>

  <path class="flow-arrow" d="M272,474 V511" marker-start="url(#head-sky)" marker-end="url(#head-sky)"/>

  <!-- step: consumer voice -->
  <g class="step step--voice">
    <circle cx="198" cy="560" r="46" fill="var(--halo)"/>
    <rect x="165" y="522" width="200" height="75" rx="37.5" fill="var(--slate)"/>
    <circle cx="210" cy="560" r="30" fill="var(--white)"/>
    <path d="M192,543 H218 V566 H204 L197,573 V566 H192 Z" class="icon-stroke" stroke="var(--slate)" stroke-width="2.2"/>
    <path d="M197,550 H213 M197,556 H210" class="icon-stroke" stroke="var(--slate)" stroke-width="2"/>
    <circle cx="221" cy="565" r="5" fill="var(--slate)"/>
    <path d="M212,580 Q221,568 230,580 Z" fill="var(--slate)"/>
    <text class="label" text-anchor="middle"><tspan x="293" y="558">CONSUMER</tspan><tspan x="293" y="572">VOICE</tspan></text>
  </g>

  <path class="flow-arrow" d="M380,425 L404,443" marker-end="url(#head-sky)"/>
  <path class="flow-arrow" d="M378,552 L404,532" marker-end="url(#head-sky)"/>

  <!-- step: interventions -->
  <g class="step step--interventions">
    <circle cx="455" cy="492" r="46" fill="var(--halo)"/>
    <rect x="420" y="455" width="200" height="75" rx="37.5" fill="var(--mint)"/>
    <circle cx="467" cy="492" r="30" fill="var(--white)"/>
    <circle cx="467" cy="492" r="11" class="icon-stroke" stroke="var(--teal)" stroke-width="5" stroke-dasharray="5 3.6"/>
    <circle cx="467" cy="492" r="5" fill="var(--teal)"/>
    <text class="label label--dark" text-anchor="middle"><tspan x="546" y="484">INTERVENTIONS</tspan><tspan x="546" y="497">TO OPTIMISE</tspan><tspan x="546" y="510">MANAGEMENT</tspan></text>
  </g>

  <path class="flow-arrow" d="M630,495 H664" marker-end="url(#head-sky)"/>

  <!-- step: outcomes -->
  <g class="step step--outcomes">
    <circle cx="727" cy="492" r="46" fill="var(--halo)"/>
    <rect x="690" y="455" width="200" height="75" rx="37.5" fill="var(--teal)"/>
    <circle cx="739" cy="492" r="30" fill="var(--white)"/>
    <path d="M723,503 L732,484 L741,498 L754,484" class="icon-stroke" stroke="var(--navy)"/>
    <path d="M726,484 L732,480 L735,487 M748,484 L755,482 L755,489" class="icon-stroke" stroke="var(--navy)" stroke-width="2.4"/>
    <text class="label" text-anchor="middle"><tspan x="818" y="478">IMPROVE</tspan><tspan x="818" y="491">OUTCOMES</tspan><tspan x="818" y="504">AND QUALITY</tspan><tspan x="818" y="517">OF LIFE</tspan></text>
  </g>

  <!-- balance panel -->
  <g class="balance">
    <rect x="507" y="591" width="392" height="207" fill="none" stroke="var(--panel-line)" stroke-width="1.5"/>
    <rect x="515" y="598" width="376" height="192" fill="var(--panel)"/>
    <rect x="625" y="765" width="183" height="14" fill="var(--navy)"/>
    <path d="M716,648 L730,765 H702 Z" fill="var(--navy)"/>
    <line x1="567" y1="700" x2="845" y2="622" stroke="var(--slate)" stroke-width="2"/>
    <path d="M567,680 Q595,702 600,722 A33,33 0 1 1 534,722 Q539,702 567,680 Z" fill="var(--slate)"/>
    <text class="label" text-anchor="middle"><tspan x="567" y="719">PATIENT</tspan><tspan x="567" y="732">WORKLOAD</tspan></text>
    <path d="M845,622 Q875,645 880,668 A35,35 0 1 1 810,668 Q815,645 845,622 Z" fill="var(--teal)"/>
    <text class="label" text-anchor="middle"><tspan x="846" y="666">PATIENT</tspan><tspan x="846" y="679">CAPACITY</tspan></text>
  </g>
</svg>
</body>
</html>
```